Allied Health team of Physiotherapists & Occupational Therapists seek a business card design

We have our new logo, we now need our new business cards and stationary. Blossom: Lymphoedema & Women's Clinic is seeking a generic card design to represent our whole team and individual cards for each therapist that incorporates our new logo to communicate our holistic approach that is calming, nuturing, supportive and welcoming.
Our Physiotherapists and Occupational Therapists assess, treat and provide education for people who are at risk of or who have lymphoedema. This is often as a result of treatment for cancer. We provide pre-operative and post-operative management and cancer rehabilitation in our Pilates studio. Our team also consists of Physiotherapists who have a strong interest in pelvic floor and continence management for both men and women.

Target Market(s)

Mainly women health conscious

Industry/Entity Type

Allied Health: Physiotherapy / Occupational Therapy

Contact Information for Business Card

Address: 14 Calloway Ave Frankston 3199 Phone: 84317560 fax: 8431 7564 Email: info@blossomcarepartners.com.au Website: blossomcarepartners.com.au Facebook address: facebook.com/BlossomLymphoedemaAndWomensCareCentre. Room to write appointments. Individual cards need to have name, office email and individual email and professional details

Requirements
Must have
• Logo as per uploaded documents

```html
<!DOCTYPE html>
<html lang="en">
<head>
<meta charset="utf-8">
<title>Blossom – Business Cards</title>
<link href="https://fonts.googleapis.com/css2?family=Arimo:wght@400;700&family=Archivo+Black&display=swap" rel="stylesheet">
<style>
  :root{
    --backdrop:#141414;
    --card:#1c1c1c;
    --peach:#f7ad7d;
    --white:#f4f4f4;
    --sage:#b9c2bb;
  }
  *{box-sizing:border-box;margin:0;padding:0}
  html,body{width:1200px;height:912px;overflow:hidden;background:var(--backdrop)}
  body{position:relative;font-family:"Arimo",Arial,sans-serif;color:var(--white)}

  .card{position:absolute;width:620px;height:378px;background:var(--card);border-radius:14px;overflow:hidden;box-shadow:0 10px 30px rgba(0,0,0,.5)}
  .card--appointment{left:60px;top:56px}
  .card--profile{left:520px;top:478px}

  /* brand stand-in */
  .brand{display:flex;align-items:center;gap:10px;color:var(--peach);font-family:"Arimo",Arial,sans-serif;font-weight:400;line-height:1}
  .brand__dot{width:14px;height:14px;border-radius:50%;background:var(--peach)}

  /* appointment side */
  .leaf-wash{position:absolute;left:-40px;top:40px;width:520px;height:360px;border-radius:50%;
    background:radial-gradient(ellipse at 60% 50%,rgba(255,255,255,.035),rgba(255,255,255,0) 70%)}
  .card--appointment .brand{position:absolute;left:0;right:0;top:60px;justify-content:center;font-size:44px}
  .appt__title{position:absolute;left:0;right:0;top:148px;text-align:center;color:var(--peach);font-size:20px}
  .appt__line{position:absolute;left:46px;right:46px;top:196px;display:flex;align-items:flex-end;gap:8px;font-size:16px}
  .appt__dots{flex:1;border-bottom:1.5px dashed var(--white);height:1px;margin-bottom:4px}
  .appt__days{position:absolute;left:46px;right:46px;top:244px;display:flex;justify-content:space-between;font-size:16px}
  .day{display:flex;align-items:center;gap:9px}
  .day__box{width:17px;height:17px;border:1.5px solid var(--white)}
  .appt__band{position:absolute;left:0;right:0;bottom:34px;height:40px;background:var(--peach);color:#1c1c1c;
    display:flex;align-items:center;justify-content:center;font-size:15px}

  /* profile side */
  .profile__bar{position:absolute;left:24px;top:94px;width:14px;height:92px;background:var(--peach)}
  .profile__name{position:absolute;left:50px;top:88px;font-family:"Archivo Black","Arimo",sans-serif;font-size:27px;line-height:34px;color:var(--peach);letter-spacing:.5px;font-weight:400}
  .profile__quals{position:absolute;left:52px;top:128px;font-size:11.5px;line-height:16px;color:var(--white)}
  .profile__roles{position:absolute;left:52px;top:196px;font-size:14.5px;line-height:19px;color:var(--sage)}
  .contact{position:absolute;left:52px;top:270px;list-style:none;font-size:13px;line-height:17px}
  .contact li{display:flex;align-items:center;gap:7px}
  .contact svg{width:12px;height:12px;fill:var(--white);flex:none}
  .card--profile .brand{position:absolute;right:48px;top:120px;font-size:42px}
</style>
</head>
<body>

<section class="card card--appointment">
  <div class="leaf-wash" role="img" aria-label="Faint leaf-sprig decoration in the background"></div>
  <div class="brand"><span class="brand__dot"></span>Blossom</div>
  <h2 class="appt__title">Your Next Appointment</h2>
  <div class="appt__line">
    <span>Date</span><span class="appt__dots"></span>
    <span>Time</span><span class="appt__dots"></span>
    <span>am/pm</span>
  </div>
  <div class="appt__days">
    <span class="day"><span class="day__box"></span>Sun</span>
    <span class="day"><span class="day__box"></span>Mon</span>
    <span class="day"><span class="day__box"></span>Tue</span>
    <span class="day"><span class="day__box"></span>Wed</span>
    <span class="day"><span class="day__box"></span>Thu</span>
    <span class="day"><span class="day__box"></span>Fri</span>
  </div>
  <div class="appt__band">www.facebook.com/BlossomLymphoedemaAndWomensCareCentre</div>
</section>

<section class="card card--profile">
  <div class="profile__bar"></div>
  <h1 class="profile__name">MARISA HOLT</h1>
  <p class="profile__quals">
    B. Physio (Hons), B.Sc.(Exercise Science/Biology)<br>
    Grad Dip. Women's Health Physiotherapy<br>
    Grad Cert. Lymphoedema &amp; Oncology Rehabilitation
  </p>
  <p class="profile__roles">
    Physiotherapist<br>
    Lymphoedema &amp; Oncology Rehabilitation<br>
    Continence &amp; Pelvic Floor
  </p>
  <ul class="contact">
    <li><svg viewBox="0 0 24 24"><path d="M6.6 10.8a15.1 15.1 0 0 0 6.6 6.6l2.2-2.2c.3-.3.7-.4 1-.2 1.1.4 2.3.6 3.6.6.6 0 1 .4 1 1V20c0 .6-.4 1-1 1A17 17 0 0 1 3 4c0-.6.4-1 1-1h3.5c.6 0 1 .4 1 1 0 1.3.2 2.5.6 3.6.1.3 0 .7-.2 1z"/></svg>8431 7560</li>
    <li><svg viewBox="0 0 24 24"><path d="M6 2h12v6H6zM4 9h16a2 2 0 0 1 2 2v6h-4v5H6v-5H2v-6a2 2 0 0 1 2-2zm4 8v3h8v-3z"/></svg>8431 7564</li>
    <li><svg viewBox="0 0 24 24"><path d="M2 5h20v14H2zm2 2v.5l8 5 8-5V7zm0 3v7h16v-7l-8 5z"/></svg>info@blossomcarepartners.com.au</li>
    <li><svg viewBox="0 0 24 24"><path d="M12 2a10 10 0 1 0 0 20 10 10 0 0 0 0-20zm6.9 9h-3a15 15 0 0 0-1.3-5.6A8 8 0 0 1 18.9 11zM12 4.1c.9 1.2 1.8 3.5 1.9 6.9h-3.8c.1-3.4 1-5.7 1.9-6.9zM9.4 5.4A15 15 0 0 0 8.1 11h-3a8 8 0 0 1 4.3-5.6zM5.1 13h3a15 15 0 0 0 1.3 5.6A8 8 0 0 1 5.1 13zm6.9 6.9c-.9-1.2-1.8-3.5-1.9-6.9h3.8c-.1 3.4-1 5.7-1.9 6.9zm2.6-1.3a15 15 0 0 0 1.3-5.6h3a8 8 0 0 1-4.3 5.6z"/></svg>www.blossomcarepartners.com.au</li>
    <li><svg viewBox="0 0 24 24"><path d="M12 2a7 7 0 0 0-7 7c0 5 7 13 7 13s7-8 7-13a7 7 0 0 0-7-7zm0 9.5a2.5 2.5 0 1 1 0-5 2.5 2.5 0 0 1 0 5z"/></svg>14 Calloway Ave, Seabrook 3928</li>
  </ul>
  <div class="brand"><span class="brand__dot"></span>Blossom</div>
</section>

</body>
</html>
```